Open sky balance Business cards - yoga studio

We need business cards for our yoga studio Openbreath Harmony.
We would like to see designs that include the colour blue and our logo.
The business card should communicate a feeling of strength and calm

Business

Requirements
Must have
• The business card must include
"Maren Tollefsen - Director"
and
"42 Quillfern Avenue
Dunmorrow
VIC 3791
Ph - 0451 628 904"

```html
<!DOCTYPE html>
<html lang="en">
<head>
<meta charset="utf-8">
<title>Openbreath Harmony – Business Cards</title>
<link rel="stylesheet" href="https://fonts.googleapis.com/css2?family=Arimo:wght@400;700&display=swap">
<style>
  :root {
    --backdrop: #5b5b5b;
    --backdrop-light: #6a6a6a;
    --teal-deep: #13758f;
    --teal-soft: #69b5c8;
    --teal-pale: #a6dbe6;
    --logo-teal: #5fb4c6;
    --paper: #ffffff;
    --ink-light: #ffffff;
  }
  * { box-sizing: border-box; margin: 0; padding: 0; }
  html, body {
    width: 1200px; height: 1000px; overflow: hidden;
  }
  body {
    background: radial-gradient(ellipse at 50% 40%, var(--backdrop-light), var(--backdrop) 75%);
    font-family: "Arimo", Arial, sans-serif;
    position: relative;
  }
  .card {
    position: absolute;
    top: 66px;
    width: 543px;
    height: 317px;
    overflow: hidden;
    box-shadow: 0 1px 3px rgba(0,0,0,.35);
  }
  .card-front { left: 40px; background: var(--teal-deep); }
  .card-back  { left: 621px; background: var(--paper); }
  .card-shape { position: absolute; inset: 0; width: 100%; height: 100%; }

  .holder {
    position: absolute; left: 317px; top: 27px;
    color: var(--ink-light);
  }
  .holder-name { font-size: 22px; font-weight: 700; line-height: 1.1; letter-spacing: .1px; }
  .holder-role { font-size: 14px; font-weight: 400; margin-top: 2px; }

  .contact-list {
    position: absolute; left: 40px; top: 207px;
    list-style: none; color: var(--ink-light);
    font-size: 14.5px; line-height: 20.5px;
  }
  .contact-list li { display: flex; align-items: center; gap: 6px; }
  .contact-icon { width: 12px; height: 12px; flex: none; }

  .brand-name {
    position: absolute; left: 0; right: 0; top: 136px;
    text-align: center;
    font-size: 34px; font-weight: 400; letter-spacing: .5px;
    color: var(--logo-teal);
  }
  .studio-address {
    position: absolute; left: 0; right: 0; top: 274px;
    text-align: center; color: var(--ink-light);
    font-size: 14.5px;
  }
</style>
</head>
<body>

  <section class="card card-front" aria-label="Business card front">
    <svg class="card-shape" viewBox="0 0 543 317" preserveAspectRatio="none" aria-hidden="true">
      <path d="M0,317 C180,300 440,250 543,128 L543,317 Z" fill="var(--teal-pale)"/>
      <path d="M0,317 C200,305 450,262 543,146 L543,317 Z" fill="var(--teal-soft)"/>
    </svg>

    <div class="holder">
      <p class="holder-name">Maren Tollefsen</p>
      <p class="holder-role">Director</p>
    </div>

    <ul class="contact-list">
      <li>
        <svg class="contact-icon" viewBox="0 0 12 12" aria-hidden="true"><rect x="3" y="0.5" width="6" height="11" rx="1.2" fill="none" stroke="#fff" stroke-width="1.2"/><rect x="4.3" y="2" width="3.4" height="5" fill="#fff"/></svg>
        0451 628 904
      </li>
      <li>
        <svg class="contact-icon" viewBox="0 0 12 12" aria-hidden="true"><path d="M3,1 L5,1 L5.6,3.6 L4.3,4.6 C5,6.3 5.9,7.3 7.4,7.9 L8.4,6.6 L11,7.2 L11,9.2 C11,10.2 10,11 9,11 C4.6,10.6 1.4,7.4 1,3 C1,2 2,1 3,1 Z" fill="#fff"/></svg>
        0451 628 904
      </li>
      <li>
        <svg class="contact-icon" viewBox="0 0 12 12" aria-hidden="true"><rect x="0.8" y="2.5" width="10.4" height="7.5" fill="none" stroke="#fff" stroke-width="1.1"/><path d="M1,3 L6,7 L11,3" fill="none" stroke="#fff" stroke-width="1.1"/></svg>
        hi@openbreath.com
      </li>
      <li>
        <svg class="contact-icon" viewBox="0 0 12 12" aria-hidden="true"><circle cx="6" cy="6" r="5.2" fill="none" stroke="#fff" stroke-width="1.1"/><ellipse cx="6" cy="6" rx="2.3" ry="5.2" fill="none" stroke="#fff" stroke-width="1"/><path d="M0.8,6 H11.2 M1.6,3.4 H10.4 M1.6,8.6 H10.4" stroke="#fff" stroke-width="0.9"/></svg>
        www.openbreath.com
      </li>
    </ul>
  </section>

  <section class="card card-back" aria-label="Business card back">
    <svg class="card-shape" viewBox="0 0 543 317" preserveAspectRatio="none" aria-hidden="true">
      <path d="M0,204 C160,262 330,278 543,168 L543,317 L0,317 Z" fill="var(--teal-pale)"/>
      <path d="M0,211 C160,268 330,283 543,178 L543,317 L0,317 Z" fill="var(--teal-deep)"/>
    </svg>

    <p class="brand-name">Openbreath Harmony</p>
    <p class="studio-address">42 Quillfern Avenue, Dunmorrow, VIC 3791</p>
  </section>

</body>
</html>
```